Need a label for food product looking original design

We need two labels designed ( Front and Back ) for our new product Freeze Dried Strawberry Pieces On the front should also be our company name Velmaro . A pack will weigh 50 grams there should also be an image included of these strawbberies please find an attached file. Also it's suitable for vegans and vegetarians On the back there should be some information included what the product is used for and nutritional facts, also an e-mail for questions or product quality to be sent to sales@velmaro.co.uk Both labels should be 16cm long and 11cm wide we'll be using stand up pouches.

Target Market(s)

Bakery, snacks.

Font styles to use
Decorative
Script

Requirements
Must have
• Company name, image of the product.Label color to blend in pouch color.
Nice to have
• Suitable for vegans and vegetarians logos.
Should not have
• Custom printed pouches are not available.

```html
<!DOCTYPE html>
<html lang="en">
<head>
<meta charset="utf-8">
<title>Velmaro Freeze Dried Strawberry Pieces – Front Label</title>
<link href="https://fonts.googleapis.com/css2?family=Kaushan+Script&family=Dancing+Script:wght@500&family=Tinos&display=swap" rel="stylesheet">
<style>
  :root {
    --band-start: #e6284a;
    --band-end: #e95d7a;
    --label-white: #ffffff;
    --page-bg: #f2f2f2;
    --accent-red: #d81f4a;
    --badge-green: #1f6b3a;
    --berry-deep: #c8203a;
    --berry-light: #f08a9b;
  }
  * { margin: 0; padding: 0; box-sizing: border-box; }
  html, body {
    width: 1200px;
    height: 703px;
    overflow: hidden;
    background: var(--page-bg);
  }
  .front-label {
    position: absolute;
    left: 372px;
    top: 21px;
    width: 456px;
    height: 660px;
    background: var(--label-white);
    overflow: hidden;
  }
  .header-band {
    position: absolute;
    left: 0;
    top: 0;
    width: 456px;
    height: 290px;
  }
  .product-title {
    position: absolute;
    left: 0;
    top: 0;
    width: 456px;
    height: 260px;
    color: var(--label-white);
    font-family: "Kaushan Script", cursive;
    font-weight: 400;
    line-height: 1;
  }
  .title-main,
  .title-fruit,
  .title-form {
    position: absolute;
    white-space: nowrap;
  }
  .title-main {
    left: 42px;
    top: 30px;
    font-size: 72px;
  }
  .title-fruit {
    left: 78px;
    top: 108px;
    font-size: 60px;
  }
  .title-form {
    left: 256px;
    top: 184px;
    font-size: 58px;
  }
  .claims {
    position: absolute;
    left: 52px;
    top: 274px;
    list-style: none;
    color: var(--accent-red);
    font-family: "Dancing Script", cursive;
    font-weight: 500;
    font-size: 24px;
    line-height: 33px;
    white-space: nowrap;
  }
  .claims li:nth-child(2) { padding-left: 17px; }
  .claims li:nth-child(3) { padding-left: 38px; }
  .vegan-badge {
    position: absolute;
    left: 306px;
    top: 331px;
    width: 64px;
    height: 64px;
  }
  .product-photo {
    position: absolute;
    left: 0;
    top: 388px;
    width: 348px;
    height: 222px;
    border-radius: 40% 50% 30% 8% / 48% 60% 40% 14%;
    background: radial-gradient(ellipse at 40% 50%, var(--berry-light) 0%, var(--berry-deep) 65%, rgba(200,32,58,0.15) 100%);
  }
  .net-weight {
    position: absolute;
    left: 47px;
    top: 618px;
    color: var(--accent-red);
    font-family: "Tinos", serif;
    font-size: 17px;
    letter-spacing: 0.5px;
  }
  .brand-name {
    position: absolute;
    left: 296px;
    top: 609px;
    color: var(--accent-red);
    font-family: "Tinos", serif;
    font-size: 29px;
  }
</style>
</head>
<body>
  <main class="front-label">
    <svg class="header-band" viewBox="0 0 456 290" aria-hidden="true">
      <defs>
        <linearGradient id="bandFill" x1="0" y1="0" x2="1" y2="0">
          <stop offset="0" stop-color="#e6284a"/>
          <stop offset="1" stop-color="#e95d7a"/>
        </linearGradient>
      </defs>
      <path d="M0 0 H456 V284 C400 282 340 260 270 248 C200 236 140 236 90 250 C55 260 25 267 0 270 Z" fill="url(#bandFill)"/>
    </svg>

    <h1 class="product-title">
      <span class="title-main">Freeze Dried</span>
      <span class="title-fruit">strawberry</span>
      <span class="title-form">pieces</span>
    </h1>

    <ul class="claims">
      <li>100% strawberry</li>
      <li>no sugar added</li>
      <li>no preservatives</li>
    </ul>

    <svg class="vegan-badge" viewBox="0 0 64 64" role="img" aria-label="Suitable for vegans and vegetarians badge">
      <circle cx="32" cy="32" r="32" fill="#1f6b3a"/>
    </svg>

    <div class="product-photo" role="img" aria-label="Photo of a pile of freeze dried strawberry pieces"></div>

    <p class="net-weight">Net 50g</p>
    <p class="brand-name">Velmaro</p>
  </main>
</body>
</html>
```